Business Card Design

Very plain simple card, Plain modern font. Background. Grey fading to black. Large Bright lime green text. Saying.

TWR-ZA.COM

Small other details in white text.

Irish Horse Sales . Livery . Stud . Shows

Mark Dabrowski
TWR
Birch Lodge
Carrowmede Lane
Thistlecombe
Lincolnshire
LN4 7JX

Email. Twrzap@mailvale.co.uk
Tel. 07482 936504

Industry/Entity Type

Business

Contact Information for Business Card

As below

```html
<!DOCTYPE html>
<html lang="en">
<head>
<meta charset="utf-8">
<title>TWR-ZA.COM Business Card</title>
<link rel="stylesheet" href="https://fonts.googleapis.com/css2?family=Ubuntu:wght@400;500;700&display=swap">
<style>
  :root {
    --stage: #bebebe;
    --stage-band: #b3b3b3;
    --card-light: #575757;
    --card-mid: #2c2c2c;
    --card-dark: #1b1b1b;
    --lime: #9ccd10;
    --white: #ffffff;
  }
  * { margin: 0; padding: 0; box-sizing: border-box; }
  html, body {
    width: 1200px;
    height: 999px;
    overflow: hidden;
    background: var(--stage);
    font-family: "Ubuntu", sans-serif;
  }
  .stage { position: relative; width: 1200px; height: 999px; }
  .stage-band {
    position: absolute; left: 0; bottom: 0;
    width: 100%; height: 25px;
    background: var(--stage-band);
  }
  .card {
    position: absolute;
    left: 267px; top: 280px;
    width: 666px; height: 438px;
    background: radial-gradient(ellipse 75% 90% at 48% 4%, var(--card-light) 0%, var(--card-mid) 50%, var(--card-dark) 85%);
    color: var(--white);
  }
  .brand {
    position: absolute;
    right: 52px; top: 83px;
    text-align: left;
  }
  .brand-name {
    font-weight: 500;
    font-size: 56px;
    line-height: 1;
    color: var(--lime);
    letter-spacing: -0.5px;
  }
  .brand-tagline {
    font-size: 19px;
    line-height: 1;
    margin-top: 5px;
    margin-left: 2px;
  }
  .person {
    position: absolute;
    left: 53px; top: 245px;
  }
  .person-name { font-size: 23px; line-height: 1.2; }
  .person-role { font-size: 16px; line-height: 1.2; margin-top: 1px; }
  .contact {
    position: absolute;
    left: 372px; top: 243px;
    font-size: 16.5px;
    line-height: 21px;
  }
  .address { margin-bottom: 21px; }
  .contact-line { display: flex; align-items: center; gap: 13px; }
  .contact-icon { width: 10px; height: 10px; flex: none; }
</style>
</head>
<body>
<div class="stage">
  <section class="card">
    <header class="brand">
      <div class="brand-name">TWR-ZA.COM</div>
      <div class="brand-tagline">Irish Horse Sales . Livery . Stud . Shows</div>
    </header>

    <div class="person">
      <div class="person-name">Mark Dabrowski</div>
      <div class="person-role">TWR</div>
    </div>

    <div class="contact">
      <address class="address" style="font-style:normal">
        Birch Lodge Carrowmede Lane<br>
        Thistlecombe Lincolnshire<br>
        LN4 7JX
      </address>
      <div class="contact-line">
        <svg class="contact-icon" viewBox="0 0 10 10" aria-label="Email">
          <rect width="10" height="10" fill="#fff"/>
          <rect x="2" y="3" width="6" height="4.2" fill="none" stroke="#222" stroke-width="0.8"/>
          <path d="M2 3 L5 5.4 L8 3" fill="none" stroke="#222" stroke-width="0.8"/>
        </svg>
        <span>Twrzap@mailvale.co.uk</span>
      </div>
      <div class="contact-line">
        <svg class="contact-icon" viewBox="0 0 10 10" aria-label="Phone">
          <rect width="10" height="10" fill="#fff"/>
          <path d="M3.2 2.2 L4.4 3.6 L3.8 4.4 Q4.6 5.8 5.8 6.4 L6.6 5.8 L8 7 L7.2 8 Q4.6 7.8 2.4 4.6 Q2.2 3.2 3.2 2.2 Z" fill="#222"/>
        </svg>
        <span>07482 936504</span>
      </div>
    </div>
  </section>
  <div class="stage-band"></div>
</div>
</body>
</html>
```